Personal Training Studio business cards

Black logo on front. Also need: Carlyse Brondway Master Trainer, Phone: 0498315627 on the front.
On the back want the white logo and also want 10 stars or similar that can be stamped when attended Studio. The 10th start to have "Free" written under it.
Also want a line to write an appointment date and time on it.

```html
<!DOCTYPE html>
<html lang="en">
<head>
<meta charset="utf-8">
<title>Ember Loft – Business Cards</title>
<link href="https://fonts.googleapis.com/css2?family=Open+Sans:wght@400;600;700;800&display=swap" rel="stylesheet">
<style>
  :root {
    --backdrop: #2b2b2b;
    --card-black: #0d0d0d;
    --card-white: #ffffff;
    --purple: #6a4a9c;
    --green: #7dbf3f;
    --star-1: #7dbf3f;
    --star-2: #7aa95a;
    --star-3: #748a78;
    --star-4: #6e6a8c;
    --star-5: #6a4a9c;
    --divider: #c9c9c9;
  }
  * { box-sizing: border-box; margin: 0; padding: 0; }
  html, body {
    width: 1200px; height: 660px; overflow: hidden;
    background: var(--backdrop);
    font-family: "Open Sans", Arial, sans-serif;
  }
  .stage {
    position: relative; width: 1200px; height: 660px;
    display: flex; align-items: center; justify-content: center; gap: 40px;
  }
  .card {
    position: relative; width: 540px; height: 310px;
    box-shadow: 0 10px 30px rgba(0,0,0,.45);
  }
  .card--front {
    background: var(--card-black);
    display: flex; align-items: center; justify-content: center;
  }
  .brand {
    display: flex; align-items: center; gap: 12px;
    font-weight: 800; color: var(--purple);
    text-transform: uppercase; letter-spacing: 1px;
  }
  .brand__dot {
    width: 26px; height: 26px; border-radius: 50%; background: var(--green);
  }
  .card--front .brand { font-size: 50px; }
  .card--front .brand__dot { width: 40px; height: 40px; }

  .card--back { background: var(--card-white); color: var(--purple); }
  .card--back .brand {
    position: absolute; left: 28px; top: 66px; font-size: 30px;
  }
  .divider {
    position: absolute; left: 250px; top: 18px; width: 1px; height: 100px;
    background: linear-gradient(to bottom, transparent, var(--divider), transparent);
  }
  .contact { position: absolute; left: 272px; top: 26px; width: 246px; }
  .contact__name { font-size: 19px; font-weight: 400; }
  .contact__name strong { font-weight: 700; }
  .contact__role { font-size: 13px; font-weight: 700; color: var(--green); margin-top: 2px; }
  .contact__phone { font-size: 15px; margin-top: 6px; padding-bottom: 8px;
    border-bottom: 2px dotted var(--purple); }

  .booking { position: absolute; left: 28px; right: 22px; font-size: 13px; font-weight: 600;
    display: flex; align-items: flex-end; gap: 6px; }
  .booking__line { flex: 1; border-bottom: 2px dotted var(--purple); height: 1px; margin-bottom: 4px; }
  .booking--appointment { top: 150px; }
  .booking--date { top: 196px; }

  .stamps { position: absolute; left: 26px; right: 22px; bottom: 22px;
    display: flex; justify-content: space-between; }
  .stamps svg { width: 40px; height: 40px; }
</style>
</head>
<body>
<main class="stage">
  <section class="card card--front">
    <div class="brand"><span class="brand__dot"></span>Ember Loft</div>
  </section>

  <section class="card card--back">
    <div class="brand"><span class="brand__dot"></span>Ember Loft</div>
    <div class="divider"></div>
    <div class="contact">
      <p class="contact__name"><strong>Carlyse</strong> Brondway</p>
      <p class="contact__role">Master Trainer</p>
      <p class="contact__phone">phone: 0498315627</p>
    </div>
    <div class="booking booking--appointment">
      <span>appointment</span><span class="booking__line"></span>
      <span>time</span><span class="booking__line"></span>
    </div>
    <div class="booking booking--date">
      <span>date</span><span class="booking__line"></span>
    </div>

    <svg width="0" height="0" style="position:absolute">
      <defs>
        <polygon id="star" points="20,2 25,15 39,15 28,24 32,38 20,30 8,38 12,24 1,15 15,15"/>
      </defs>
    </svg>
    <div class="stamps" aria-label="Ten attendance stamp stars">
      <svg viewBox="0 0 40 40"><use href="#star" fill="var(--star-1)"/></svg>
      <svg viewBox="0 0 40 40"><use href="#star" fill="var(--star-1)"/></svg>
      <svg viewBox="0 0 40 40"><use href="#star" fill="var(--star-1)"/></svg>
      <svg viewBox="0 0 40 40"><use href="#star" fill="var(--star-1)"/></svg>
      <svg viewBox="0 0 40 40"><use href="#star" fill="var(--star-2)"/></svg>
      <svg viewBox="0 0 40 40"><use href="#star" fill="var(--star-2)"/></svg>
      <svg viewBox="0 0 40 40"><use href="#star" fill="var(--star-3)"/></svg>
      <svg viewBox="0 0 40 40"><use href="#star" fill="var(--star-4)"/></svg>
      <svg viewBox="0 0 40 40"><use href="#star" fill="var(--star-5)"/></svg>
      <svg viewBox="0 0 40 40"><use href="#star" fill="var(--star-5)"/></svg>
    </div>
  </section>
</main>
</body>
</html>
```